We need visit card and a letter paper for our website. thx

We have a beauty clinic in Switzerland.
https://wiesentalblick.ch
We need a visit card.

Requirements
Must have
• see colors on website

```html
<!DOCTYPE html>
<html lang="de">
<head>
<meta charset="utf-8">
<title>Wiesentalblick – Visitenkarte</title>
<link rel="stylesheet" href="https://fonts.googleapis.com/css2?family=Marcellus&family=Roboto:wght@400;500&display=swap">
<style>
  :root {
    --bg: #e4e4e4;
    --card-white: #ffffff;
    --card-dark: #2f2f31;
    --accent: #e0317b;
    --ink: #111111;
    --ink-soft: #4a4a4a;
    --light: #f4f4f4;
  }
  * { box-sizing: border-box; margin: 0; padding: 0; }
  html, body { width: 1200px; height: 801px; overflow: hidden; }
  body {
    background: var(--bg);
    font-family: "Roboto", Arial, sans-serif;
    display: flex;
    align-items: center;
    justify-content: center;
    gap: 60px;
  }
  .card {
    width: 520px;
    height: 297px;
    border-bottom: 3px solid var(--accent);
    position: relative;
    box-shadow: 0 6px 18px rgba(0,0,0,.12);
  }
  .card--front { background: var(--card-white); display: flex; }
  .card--back {
    background: var(--card-dark);
    display: flex; align-items: center; justify-content: center;
  }
  .brand {
    font-family: "Marcellus", Georgia, serif;
    font-weight: 400;
    font-size: 38px;
    letter-spacing: .5px;
    color: var(--ink);
    display: flex; align-items: center; gap: 12px;
  }
  .brand__square {
    width: 12px; height: 12px;
    border: 1px solid currentColor;
  }
  .card--back .brand { color: var(--light); font-size: 46px; }
  .front__logo {
    width: 56%;
    display: flex; align-items: center; justify-content: center;
  }
  .front__info {
    width: 44%;
    border-left: 1.5px solid var(--accent);
    margin: 58px 0;
    padding-left: 18px;
    display: flex; flex-direction: column; justify-content: center;
  }
  .names {
    color: var(--accent);
    font-weight: 500;
    font-size: 15px;
    line-height: 1.3;
    margin-bottom: 12px;
  }
  .address, .contact {
    color: var(--ink-soft);
    font-size: 12.5px;
    line-height: 1.45;
  }
  .address { margin-bottom: 10px; }
  .contact li { list-style: none; display: flex; align-items: center; gap: 6px; }
  .contact svg { width: 11px; height: 11px; fill: var(--accent); flex: none; }
</style>
</head>
<body>
  <section class="card card--front">
    <div class="front__logo">
      <div class="brand"><span class="brand__square"></span>Wiesentalblick</div>
    </div>
    <div class="front__info">
      <p class="names">Dr. Lea Marbach<br>Dr. Simon Altherr, DESA</p>
      <p class="address">Talweg 24<br>7530 Zernez, Switzerland</p>
      <ul class="contact">
        <li><svg viewBox="0 0 24 24"><path d="M6.6 10.8a15.1 15.1 0 0 0 6.6 6.6l2.2-2.2a1 1 0 0 1 1-.25 11.4 11.4 0 0 0 3.6.57 1 1 0 0 1 1 1V20a1 1 0 0 1-1 1A17 17 0 0 1 3 4a1 1 0 0 1 1-1h3.5a1 1 0 0 1 1 1c0 1.25.2 2.45.57 3.57a1 1 0 0 1-.25 1z"/></svg>+41 (0) 800 22 40 40</li>
        <li><svg viewBox="0 0 24 24"><path d="M2 5h20v14H2z M2 5l10 8 10-8" fill="var(--accent)"/><path d="M3 6l9 7 9-7" fill="none" stroke="#fff" stroke-width="1.5"/></svg>hallo@wiesentalblick.ch</li>
        <li><svg viewBox="0 0 24 24"><circle cx="12" cy="12" r="10"/><path d="M2 12h20M12 2c3 3 3 17 0 20M12 2c-3 3-3 17 0 20" stroke="#fff" stroke-width="1.3" fill="none"/></svg>wiesentalblick.ch</li>
      </ul>
    </div>
  </section>
  <section class="card card--back">
    <div class="brand"><span class="brand__square"></span>Wiesentalblick</div>
  </section>
</body>
</html>
```